Outlast the Coming Storm - book cover

A book cover (front) to be used on print book. Book will be 5 inches by 8 inches. Also need the cover image (as jpg) for promotional purposes. Include company logo on cover - I've included a couple of versions. Include my name as author: Dr. Corliss Vandemeer

Title of book is:
Weathering Every Market Tide
(sub-title) through coaching clear reasoning

this can be a sub-sub title, or a call out or "burst" standing alone -
A survival guide for 21st century business

If you'd like some inspiration, check out my web page: www.mentorvale.com
The company colors are red, white and blue, but I think red might be too harsh - use with caution if you use it.
RGB values of the company are:
Blue: 0/66/105
Red: 190/30/45

Target Market(s)

Business / Professionals / Chief Executives of Companies with more than 1000 employees

Industry/Entity Type

Business

Font styles to use
Serif

Colors
0255a3
ffffff

Requirements
Must have
• The title should make them pause and say "I need to get this book if I want my company to survive another 20 years!"
Nice to have
• Some image that signifies the future and / or uncertainty. Should be abstract - not people, not technology (which could change and then make the book look old). If you'd like to make the design a wrap from front to back, that is fine. I am not sure what text will go on the back at this point, so I may have to come back to you in a few months for an update.

```html
<!DOCTYPE html>
<html lang="en">
<head>
<meta charset="utf-8">
<title>Weathering Every Market Tide — Dr. Corliss Vandemeer</title>
<link rel="stylesheet" href="https://fonts.googleapis.com/css2?family=Noto+Serif:ital,wght@1,400&family=Open+Sans:wght@400;600;800&family=Orbitron:wght@600&display=swap">
<style>
  :root {
    --page: #ffffff;
    --night: #061a33;
    --deep: #0a2e57;
    --glow: #2fb4e0;
    --ink: #000000;
    --brand-blue: #0255a3;
    --title-blue: #2a7fd0;
    --navy: #004269;
    --accent-red: #be1e2d;
    --white: #ffffff;
  }
  * { margin: 0; padding: 0; box-sizing: border-box; }
  html, body {
    width: 960px; height: 1200px; overflow: hidden;
    background: var(--page);
  }
  .canvas {
    width: 960px; height: 1200px;
    display: flex; justify-content: center;
  }
  .cover {
    position: relative;
    width: 750px; height: 1200px;
    background: var(--white);
    overflow: hidden;
  }
  .cover-art {
    position: absolute; left: 0; top: 0;
    width: 750px; height: 720px;
    background:
      radial-gradient(circle at 46% 30%, rgba(47,180,224,0.75) 0, rgba(47,180,224,0.25) 18%, rgba(10,46,87,0) 42%),
      linear-gradient(180deg, var(--night) 0%, var(--deep) 45%, #14487e 72%, var(--ink) 92%);
  }
  .title-band {
    position: absolute; left: 0; top: 560px;
    width: 750px; height: 230px;
    background: linear-gradient(180deg, rgba(0,0,0,0) 0%, var(--ink) 30%, var(--ink) 62%, var(--brand-blue) 100%);
  }
  .reflection-art {
    position: absolute; left: 0; top: 780px;
    width: 750px; height: 360px;
    background: linear-gradient(180deg, var(--brand-blue) 0%, rgba(2,85,163,0.55) 35%, rgba(2,85,163,0.12) 75%, rgba(255,255,255,0) 100%);
  }
  .author {
    position: absolute; left: 0; top: 38px; width: 750px;
    text-align: center;
    font-family: "Noto Serif", Georgia, serif;
    font-style: italic;
    font-size: 60px;
    color: var(--white);
    text-shadow: 2px 3px 4px rgba(0,0,0,0.7);
    transform: rotate(-4deg);
  }
  .title {
    position: absolute; left: 36px; top: 500px; width: 690px;
    font-family: "Open Sans", Arial, sans-serif;
    font-weight: 600;
    color: var(--white);
    text-shadow: 2px 3px 4px rgba(0,0,0,0.6);
    line-height: 1.1;
  }
  .title-line { display: block; font-size: 74px; white-space: nowrap; }
  .title-line--second { padding-left: 0; }
  .title-key {
    font-family: "Orbitron", "Open Sans", sans-serif;
    font-size: 52px;
    color: var(--title-blue);
    letter-spacing: 1px;
  }
  .subtitle {
    position: absolute; left: 0; top: 790px; width: 750px;
    text-align: center;
    font-family: "Open Sans", Arial, sans-serif;
    font-weight: 800;
    font-size: 40px;
    color: var(--ink);
  }
  .brand {
    position: absolute; right: 60px; top: 1050px;
    text-align: right;
    font-family: "Open Sans", Arial, sans-serif;
    color: var(--navy);
  }
  .brand-name {
    display: flex; align-items: center; justify-content: flex-end; gap: 10px;
    font-size: 62px; font-weight: 800; line-height: 1;
  }
  .brand-dot {
    width: 14px; height: 14px; border-radius: 50%;
    background: var(--accent-red);
  }
  .brand-tagline {
    margin-top: 8px;
    font-size: 17px; font-weight: 400;
  }
</style>
</head>
<body>
  <main class="canvas">
    <section class="cover">
      <div class="cover-art" role="img" aria-label="Night city skyline beneath glowing concentric energy rings and a starry sky"></div>
      <div class="title-band"></div>
      <div class="reflection-art" role="img" aria-label="Blue mirrored reflection of the city skyline dripping downward"></div>

      <p class="author">Dr. Corliss Vandemeer</p>

      <h1 class="title">
        <span class="title-line"><span class="title-key">WEATHERING</span> Every</span>
        <span class="title-line title-line--second">Market Tide</span>
      </h1>

      <p class="subtitle">through coaching clear reasoning</p>

      <div class="brand">
        <div class="brand-name"><span class="brand-dot"></span>Mentorvale</div>
        <p class="brand-tagline">we make team coaching clearer</p>
      </div>
    </section>
  </main>
</body>
</html>
```